Flyer-Design für Unkrautbekämpfung
Sehr gute und nette Zusammenarbeit. Auch auf Änderungswünsche nach Beendigung der Contest-Phase wurde schnell eingegangen. Gerne wieder, sehr zu empfehlen!
Zielgruppe
Unkrautbekämpfung mit dem Heißwasser-Schaum-System. In Eigenleistung und Vermietung des Geräts.
Zielgruppe: Privatleute mit eigenem Grundstück, Landwirte, kleine Geschäfte (Restaurants, Läden mit Parkplatz etc.)
Aufgabenstellung
Link zur Website: www.beetglanz-service.net
Der Kreativität sind keine Grenzen gesetzt.
Bitte Vorder- und Rückseite designen. Auf der Rückseite können hauptsächlich Kontaktinformationen sein.

```html
<!DOCTYPE html>
<html lang="de">
<head>
<meta charset="utf-8">
<title>Krautfrei – Flyer Vorder- und Rückseite</title>
<link rel="stylesheet" href="https://fonts.googleapis.com/css2?family=Arimo:wght@400;700&display=swap">
<style>
  :root{
    --board:#0d2a10;
    --paper:#ffffff;
    --brand:#2e7d32;
    --brand-light:#5cb746;
    --brand-pale:#a9d69c;
    --brand-mist:#d9eed3;
    --grass-dark:#1f5a17;
    --orange:#f7941d;
    --ink:#2b2b2b;
    --ink-dark:#1a1a1a;
    --url-box:#3a3a3a;
    --stone:#8f9a8c;
    --stone-dark:#6f7c6c;
  }
  *{margin:0;padding:0;box-sizing:border-box}
  html,body{width:849px;height:1200px;overflow:hidden;background:var(--board)}
  body{position:relative;font-family:"Arimo",Arial,sans-serif;color:var(--ink)}
  .page{position:absolute;left:274.5px;width:300px;height:423px;background:var(--paper);overflow:hidden}
  .page--front{top:152.6px}
  .page--back{top:624.7px}
  .abs{position:absolute}

  /* front */
  .brand{left:15.7px;top:18px}
  .brand__mark{width:28px;height:28px;background:var(--brand)}
  .brand__text{position:absolute;left:38px;top:6px;white-space:nowrap;color:var(--brand)}
  .brand__name{font-size:12.5px;line-height:13px}
  .brand__tag{font-size:8.4px;line-height:11px}
  .hero{left:0;top:60.6px;width:300px;height:117.7px;
    background:
      radial-gradient(ellipse 60% 35% at 52% 52%,rgba(232,200,150,.75),rgba(232,200,150,0) 70%),
      radial-gradient(ellipse 40% 30% at 18% 70%,rgba(214,120,70,.55),rgba(214,120,70,0) 70%),
      linear-gradient(180deg,#a992c4 0%,#d48fbd 16%,#c9a7b0 28%,#b6a283 40%,#93806a 55%,#5e7a34 68%,#4f7f2b 82%,#9ea596 90%,#3e6a22 100%)}
  .band-top{left:0;top:53.8px}
  .band-bottom{left:0;top:178.3px}
  .headline{left:23px;top:201px;font-size:10px;line-height:11.2px;font-weight:400;color:var(--ink)}
  .rule{left:14px;top:242px;width:137.6px;height:2.4px;background:var(--orange)}
  .method-art{left:175px;top:195px;width:112.5px;height:94px;
    background:
      radial-gradient(ellipse 45% 40% at 72% 40%,rgba(92,183,70,.35),rgba(92,183,70,0) 75%),
      radial-gradient(ellipse 30% 25% at 45% 62%,rgba(40,30,90,.35),rgba(40,30,90,0) 75%),
      linear-gradient(135deg,#fafafa,#eef5ec)}
  .body-front{left:14px;top:254px;width:240px;font-size:6.9px;line-height:7.6px;color:var(--ink)}
  .body-front p{margin-bottom:7.6px}
  .body-front b{color:var(--ink-dark)}
  .seal{left:225px;top:352px}
  .footer-grass{left:0;top:400px;width:300px;height:23px;
    background:linear-gradient(180deg,var(--grass-dark) 0%,#2f7a22 45%,#58a63a 80%,#3e7f28 100%)}
  .url-box{left:86.8px;top:402px;width:126px;height:13px;background:var(--url-box);
    color:#fff;font-size:8.6px;line-height:13px;text-align:center}

  /* back */
  .chart{left:34px;top:33px}
  .claims{left:138.5px;top:41px;font-size:9.9px;line-height:11.2px;color:var(--ink-dark)}
  .section-title{left:14px;top:135px;font-size:13px;line-height:14px;font-weight:400;color:var(--ink-dark)}
  .body-back{left:14.5px;top:166px;width:280px;font-size:8.1px;line-height:9.1px;color:var(--ink-dark)}
  .body-back p{margin-bottom:9.1px}
  .contact{left:23.5px;top:313px;color:var(--brand)}
  .contact__addr{font-size:8.6px;line-height:9.6px;margin-bottom:5px}
  .contact__row{display:flex;align-items:center;gap:4px;font-size:7.4px;line-height:10.7px}
  .contact__row svg{width:6px;height:6px;fill:var(--brand)}
  .contact__url{font-size:8.6px;line-height:12px}
  .vat{left:0;width:300px;top:390px;text-align:center;font-size:7px;color:var(--brand)}
</style>
</head>
<body>

<section class="page page--front">
  <div class="abs brand">
    <div class="brand__mark"></div>
    <div class="brand__text">
      <div class="brand__name">Krautfrei</div>
      <div class="brand__tag">Biologische Unkrautvernichtung</div>
    </div>
  </div>

  <svg class="abs band-top" width="300" height="7" viewBox="0 0 300 7">
    <polygon points="78,7 86,0 300,0 300,7" fill="var(--brand)"/>
  </svg>

  <div class="abs hero" role="img" aria-label="Foto eines Einfamilienhauses mit beleuchteter Veranda, gepflegtem Rasen und Vorgarten in der Abenddämmerung"></div>

  <svg class="abs band-bottom" width="300" height="7" viewBox="0 0 300 7">
    <polygon points="0,0 213,0 221,7 0,7" fill="var(--brand-light)"/>
  </svg>

  <h1 class="abs headline">Flächenpflege mit dem<br>Heißwasser-/Ökoschaum-<br>Verfahren</h1>
  <div class="abs rule"></div>

  <div class="abs method-art" role="img" aria-label="Illustration einer Person, die mit einer Heißwasserlanze Unkraut zwischen Pflastersteinen behandelt"></div>

  <div class="abs body-front">
    <p>Bei dieser Technik wird so viel Wärme in die Pflanze<br>gebracht, dass das Eiweiß in den Zellen gerinnt und<br>die Pflanze stark geschädigt wird oder abstirbt</p>
    <p>Hierzu ist es erforderlich, eine <b>Temperatur von 65°C</b><br>über einen längeren Zeitraum an den Pflanzen zu halten.</p>
    <p>Dies wird durch das zusätzliche Ausbringen des <b>ökologisch</b> abbaubaren<br><b>Schaums gewährleistet.</b></p>
    <p>Der Schaumteppich verlangsamt das Abkühlen des Wassers. Die Hitze wirkt<br>länger und damit intensiver an der Pflanze. <b>Umliegende Unkrautsamen<br>werden mit erfasst.</b></p>
  </div>

  <svg class="abs seal" width="42" height="42" viewBox="0 0 42 42" role="img" aria-label="Siegel">
    <circle cx="21" cy="21" r="21" fill="var(--brand-light)"/>
    <circle cx="21" cy="21" r="12" fill="none" stroke="#fff" stroke-width="1.4"/>
  </svg>

  <div class="abs footer-grass" role="img" aria-label="Rasenstreifen"></div>
  <div class="abs url-box">www.beetglanz-service.net</div>
</section>

<section class="page page--back">
  <svg class="abs chart" width="92" height="86" viewBox="0 0 92 86" role="img" aria-label="Kreisdiagramm mit Fotos von Pflasterflächen vor und nach der Behandlung">
    <!-- wedges around centre (45,48), r=36, from bottom clockwise through left and top to right -->
    <path d="M45 48 L45 84 A36 36 0 0 1 19.5 73.5 Z" fill="var(--stone)"/>
    <path d="M45 48 L19.5 73.5 A36 36 0 0 1 9 48 Z" fill="#9fb0a6"/>
    <path d="M45 48 L9 48 A36 36 0 0 1 19.5 22.5 Z" fill="var(--stone-dark)"/>
    <path d="M45 48 L19.5 22.5 A36 36 0 0 1 45 12 Z" fill="var(--brand-light)"/>
    <path d="M45 48 L45 12 A36 36 0 0 1 70.5 22.5 Z" fill="var(--brand-pale)"/>
    <path d="M45 48 L70.5 22.5 A36 36 0 0 1 81 48 Z" fill="var(--brand-mist)"/>
    <path d="M45 48 L32 35 A18 18 0 0 1 45 30 Z" fill="var(--stone)" opacity=".8"/>
    <path d="M45 48 L45 30 A18 18 0 0 1 63 48 Z" fill="var(--stone-dark)" opacity=".8"/>
    <path d="M45 88 A40 40 0 1 1 85 48" fill="none" stroke="var(--brand-pale)" stroke-width="0.8"/>
    <g stroke="#fff" stroke-width="0.8">
      <line x1="45" y1="48" x2="45" y2="84"/><line x1="45" y1="48" x2="19.5" y2="73.5"/>
      <line x1="45" y1="48" x2="9" y2="48"/><line x1="45" y1="48" x2="19.5" y2="22.5"/>
      <line x1="45" y1="48" x2="45" y2="12"/><line x1="45" y1="48" x2="70.5" y2="22.5"/>
    </g>
    <circle cx="54" cy="60" r="1" fill="var(--brand-light)"/>
  </svg>

  <div class="abs claims">
    100% biologisch abbaubar<br>
    • umweltfreundlich<br>
    • nicht gesundheitsschädlich
  </div>

  <h2 class="abs section-title">Ökologie und Umwelt</h2>

  <div class="abs body-back">
    <p>Mit dem Heißwasser- /Heißwasser-Schaumverfahren wird Unkraut unter<br>strikter Beachtung des Pflanzenschutzgesetzes umweltfreundlich, effizient<br>und rein ökologisch beseitigt.</p>
    <p>Der ThermoVerde Bio-Schaum® ist in die Betriebsmittelliste für<br>ökologischen Landbau aufgenommen und erfordert keine Genehmigung für<br>das Ausbringen.</p>
    <p>Der biologisch-organische Schaum ist ein Produkt auf Basis nichtionischer<br>Tenside. Dieser wird aus nachhaltigem Anbau nachwachsender Rohstoffe<br>gewonnen.</p>
    <p>Der Schaum hinterlässt beim Trockenen keine Spuren und ist bereits nach<br>kurzer Zeit nicht mehr sichtbar.</p>
  </div>

  <div class="abs contact">
    <div class="contact__addr">Str. 93<br>31599 Moorfeld</div>
    <div class="contact__row">
      <svg viewBox="0 0 24 24"><path d="M6.6 10.8a15 15 0 0 0 6.6 6.6l2.2-2.2c.3-.3.7-.4 1-.2 1.1.4 2.3.6 3.6.6.6 0 1 .4 1 1V20c0 .6-.4 1-1 1A17 17 0 0 1 3 4c0-.6.4-1 1-1h3.5c.6 0 1 .4 1 1 0 1.3.2 2.5.6 3.6.1.3 0 .7-.2 1z"/></svg>
      05071 - 4402
    </div>
    <div class="contact__row">
      <svg viewBox="0 0 24 24"><path d="M7 1h10a2 2 0 0 1 2 2v18a2 2 0 0 1-2 2H7a2 2 0 0 1-2-2V3a2 2 0 0 1 2-2zm0 3v14h10V4z"/></svg>
      0160-5512893
    </div>
    <div class="contact__row">
      <svg viewBox="0 0 24 24"><path d="M2 5h20v14H2zm2 2v.5l8 5 8-5V7z"/></svg>
      info@beetglanz-service.net
    </div>
    <div class="contact__url">www.beetglanz-service.net</div>
  </div>

  <div class="abs vat">ID PPN: De204571186</div>
</section>

</body>
</html>
```